Tervolan Pty Ltd professional business card

A professional business card template using the colours from the supplied logo.
Clean crisp lines while, Modern while not being over the top.

Target Market(s)

Construction, commerical and industrial

Industry/Entity Type

Communications

Contact Information for Business Card

For a Communications, IT, Optical fibre installation company

Colors
37b8a4

```html
<!DOCTYPE html>
<html lang="en">
<head>
<meta charset="utf-8">
<title>Tervolan Pty Ltd – Business Card</title>
<link rel="stylesheet" href="https://fonts.googleapis.com/css2?family=Arimo:wght@400;700&display=swap">
<style>
  :root {
    --stage: #b9c8c7;
    --paper: #ffffff;
    --teal: #2fb8a6;
    --slate: #56676d;
    --edge: #2f3a3c;
    --ink-light: #ffffff;
  }
  * { box-sizing: border-box; margin: 0; padding: 0; }
  html, body {
    width: 1000px;
    height: 1200px;
    overflow: hidden;
    background: var(--stage);
    font-family: "Arimo", Arial, sans-serif;
  }
  .canvas { position: relative; width: 1000px; height: 1200px; }
  .card {
    position: absolute;
    left: 26px;
    width: 948px;
    height: 542px;
    background: var(--paper);
    overflow: hidden;
  }
  .card--front { top: 38px; }
  .card--back { top: 633px; }
  .card__shape { position: absolute; inset: 0; width: 948px; height: 542px; }

  .brand-name {
    position: absolute;
    font-weight: 700;
    color: var(--slate);
    letter-spacing: 1px;
    white-space: nowrap;
    display: flex;
    align-items: center;
  }
  .brand-name__dot {
    display: inline-block;
    background: var(--teal);
    border-radius: 50%;
  }
  .card--front .brand-name { left: 532px; top: 62px; font-size: 64px; gap: 14px; }
  .card--front .brand-name__dot { width: 30px; height: 30px; }
  .card--back .brand-name { left: 190px; top: 240px; font-size: 104px; gap: 22px; }
  .card--back .brand-name__dot { width: 46px; height: 46px; }

  .person { position: absolute; left: 474px; top: 246px; color: var(--ink-light); }
  .person__name { font-size: 27px; font-weight: 700; line-height: 1.1; }
  .person__role { font-size: 20px; margin-top: 10px; }

  .contact-list {
    position: absolute;
    left: 510px;
    top: 344px;
    list-style: none;
    color: var(--ink-light);
    font-size: 20px;
    line-height: 27px;
  }
  .contact-list__item { display: flex; align-items: flex-start; margin-bottom: 9px; }
  .contact-list__icon { width: 18px; height: 22px; margin-right: 14px; margin-top: 3px; flex: none; }

  .web-row {
    position: absolute;
    left: 248px;
    top: 507px;
    display: flex;
    align-items: center;
    color: var(--ink-light);
    font-size: 20px;
  }
  .web-row__icon { width: 20px; height: 20px; margin-right: 15px; }
  .web-row__divider { margin: 0 48px 0 58px; }
  .web-row__at { font-weight: 700; margin-right: 17px; font-size: 22px; }
</style>
</head>
<body>
<main class="canvas">

  <section class="card card--front" aria-label="Business card front">
    <svg class="card__shape" viewBox="0 0 948 542" aria-hidden="true">
      <path d="M0 542 L0 470 C40 300 300 215 948 158 L948 542 Z" fill="var(--teal)"/>
    </svg>

    <div class="brand-name"><span class="brand-name__dot"></span>Tervolan</div>

    <div class="person">
      <p class="person__name">Type your name here</p>
      <p class="person__role">Designation</p>
    </div>

    <ul class="contact-list">
      <li class="contact-list__item">
        <svg class="contact-list__icon" viewBox="0 0 18 22" aria-hidden="true">
          <rect x="3" y="1" width="12" height="20" rx="2" fill="none" stroke="#fff" stroke-width="2"/>
        </svg>
        + 00 123 456 XXX XX mobile #
      </li>
      <li class="contact-list__item">
        <svg class="contact-list__icon" viewBox="0 0 18 22" aria-hidden="true">
          <path d="M3 2 C1 4 1 8 4 13 C7 18 11 20 14 20 L16 17 L12 14 L10 16 C8 15 6 12 5 9 L7 7 L5 2 Z" fill="#fff"/>
        </svg>
        + 41 (0) 800 55 20 40 land #
      </li>
      <li class="contact-list__item">
        <svg class="contact-list__icon" viewBox="0 0 18 22" aria-hidden="true">
          <path d="M9 1 C4.5 1 2 4.5 2 8 C2 13 9 21 9 21 C9 21 16 13 16 8 C16 4.5 13.5 1 9 1 Z M9 5 A3 3 0 1 1 9 11 A3 3 0 1 1 9 5 Z" fill="#fff" fill-rule="evenodd"/>
        </svg>
        <span>Address line 1, Address line 2,<br>Country</span>
      </li>
    </ul>

    <div class="web-row">
      <svg class="web-row__icon" viewBox="0 0 20 20" aria-hidden="true">
        <g fill="none" stroke="#fff" stroke-width="1.5">
          <circle cx="10" cy="10" r="8.5"/>
          <ellipse cx="10" cy="10" rx="4" ry="8.5"/>
          <line x1="1.5" y1="10" x2="18.5" y2="10"/>
          <path d="M3 5.5 H17 M3 14.5 H17"/>
        </g>
      </svg>
      <span>www.websitedomain.com</span>
      <span class="web-row__divider">|</span>
      <span class="web-row__at">@</span>
      <span>email@websitedomain.com</span>
    </div>
  </section>

  <section class="card card--back" aria-label="Business card back">
    <svg class="card__shape" viewBox="0 0 948 542" aria-hidden="true">
      <path d="M254 0 L948 0 L948 542 L484 542 Z" fill="var(--teal)"/>
      <path d="M254 0 L484 542" stroke="var(--edge)" stroke-width="1.5" fill="none"/>
    </svg>
    <div class="brand-name"><span class="brand-name__dot"></span>Tervolan</div>
  </section>

</main>
</body>
</html>
```